Pictures required on web page

I would like change three existing pictures on my new website.

The site can be found here:
http://maplebarrelvaults.quillstudio.com.au/

The three pictures to be changed are on the home page:
Purchase- Mixed Packs
Wine Club - Let Us Choose
Education- Wine Courses

I would like somthing stylish, classic and understated that fits in with the theme and feel of the site. I know stylish is a subjective thing. At the moment, the current picture makes the text difficult to read on a destop. Plus I don't think they are a perfect fit for our website anyway. I've attached a photo of our wine course room and also me in the store. Please, don't feel as though you have to use these pictures, but they're there if you want them. However I'm open to completely different photos/graphics to be used.

```html
<!DOCTYPE html>
<html lang="en">
<head>
<meta charset="utf-8">
<title>Maplebarrel — Small winery specialist</title>
<link rel="stylesheet" href="https://fonts.googleapis.com/css2?family=Roboto:wght@400;500;700;900&family=Roboto+Condensed:wght@400&family=Roboto+Slab:wght@700&display=swap">
<style>
  :root {
    --header-top: #2f4069;
    --header-bottom: #1f2b4b;
    --menu-bar: #182139;
    --white: #ffffff;
    --muted: #c9d1e3;
    --search-bg: #3b4d78;
    --search-border: #5a6d98;
    --divider: #46577f;
    --shipping-red: #c0504d;
    --news-navy: #233157;
    --frame-line: rgba(255,255,255,0.35);
    --photo-room: #3c2a22;
    --photo-store: #3a2a22;
    --photo-front: #3e3f42;
  }
  * { box-sizing: border-box; margin: 0; padding: 0; }
  html, body { width: 1200px; height: 600px; overflow: hidden; background: var(--white); }
  body { position: relative; font-family: "Roboto", Arial, sans-serif; color: var(--white); }

  .site-header {
    position: absolute; left: 0; top: 0; width: 1200px; height: 95px;
    background: linear-gradient(var(--header-top), var(--header-bottom));
  }
  .brand { position: absolute; left: 60px; top: 4px; }
  .brand-name { font-weight: 700; font-size: 38px; line-height: 44px; letter-spacing: -0.5px; }
  .brand-tagline { font-size: 19px; color: var(--muted); margin-top: -2px; }

  .search {
    position: absolute; left: 368px; top: 18px; width: 316px; height: 35px;
    background: var(--search-bg); border: 1px solid var(--search-border); border-radius: 3px;
    display: flex; align-items: center; padding-left: 12px;
    font-size: 16px; color: var(--muted);
  }
  .search svg { position: absolute; right: 10px; top: 5px; }

  .utility-nav { position: absolute; left: 717px; top: 10px; display: flex; }
  .utility-link {
    width: 88px; height: 48px; display: flex; flex-direction: column; align-items: center;
    justify-content: space-between; font-size: 13px; color: var(--muted);
    border-left: 1px solid var(--divider);
  }
  .utility-link:first-child { border-left: none; }

  .menu-bar {
    position: absolute; left: 0; top: 95px; width: 1200px; height: 52px; background: var(--menu-bar);
    font-family: "Roboto Condensed", Arial, sans-serif; font-size: 20px;
  }
  .menu-bar ul { list-style: none; display: flex; position: absolute; left: 60px; top: 14px; gap: 33px; }
  .cart { position: absolute; left: 978px; top: 14px; display: flex; align-items: center; gap: 8px; font-family: "Roboto", Arial, sans-serif; font-size: 14px; }

  .tile { position: absolute; display: flex; flex-direction: column; align-items: center; justify-content: center; text-align: center; }
  .tile-photo { position: absolute; inset: 0; }
  .tile-kicker { position: relative; font-family: "Roboto Slab", Georgia, serif; font-weight: 700; font-size: 16px; }
  .tile-title { position: relative; font-weight: 700; font-size: 33px; line-height: 36px; }

  .courses { left: 38px; top: 164px; width: 359px; height: 240px; }
  .courses .tile-photo { background: linear-gradient(160deg, #5a3b2c, var(--photo-room) 60%, #2a1c17); }
  .packs { left: 801px; top: 164px; width: 359px; height: 240px; }
  .packs .tile-photo { background: linear-gradient(180deg, #58595c, var(--photo-front) 50%, #26272a); }
  .club { left: 418px; top: 164px; width: 361px; height: 414px; justify-content: flex-start; }
  .club .tile-photo { background: linear-gradient(110deg, #4a3328, var(--photo-store) 55%, #1f1713); }
  .club .tile-kicker { margin-top: 128px; }
  .club .tile-title { margin-top: 20px; }
  .read-more {
    position: relative; margin-top: 122px; border: 2px solid var(--white); padding: 2px 6px;
    font-family: "Roboto Slab", Georgia, serif; font-weight: 700; font-size: 16px;
  }

  .promo { position: absolute; width: 359px; height: 161px; padding: 20px 23px; }
  .promo-frame {
    width: 100%; height: 100%; border: 1px solid var(--frame-line);
    display: flex; flex-direction: column; align-items: center; justify-content: center;
  }
  .promo-title { font-size: 21px; letter-spacing: 2.5px; font-weight: 400; }
  .promo-sub { font-size: 15px; letter-spacing: 1.5px; margin-top: 6px; }
  .shipping { left: 38px; top: 420px; background: var(--shipping-red); }
  .newsletter { left: 801px; top: 418px; background: var(--news-navy); }
</style>
</head>
<body>
  <header class="site-header">
    <div class="brand">
      <div class="brand-name">Maplebarrel</div>
      <div class="brand-tagline">Small winery specialist.</div>
    </div>
    <div class="search">Search the Cellars
      <svg width="26" height="26" viewBox="0 0 26 26"><circle cx="11" cy="11" r="8" fill="none" stroke="#fff" stroke-width="2.2"/><line x1="17" y1="17" x2="24" y2="24" stroke="#fff" stroke-width="3" stroke-linecap="round"/></svg>
    </div>
    <nav class="utility-nav">
      <div class="utility-link"><svg width="20" height="18" viewBox="0 0 20 18"><path d="M10 1 1 9h3v8h4v-5h4v5h4V9h3z" fill="#c9d1e3"/></svg>HOME</div>
      <div class="utility-link"><svg width="24" height="18" viewBox="0 0 24 18"><circle cx="12" cy="5" r="4" fill="#c9d1e3"/><circle cx="4.5" cy="6" r="3" fill="#c9d1e3"/><circle cx="19.5" cy="6" r="3" fill="#c9d1e3"/><path d="M5 18c0-5 3-8 7-8s7 3 7 8zM0 16c0-4 2-6 5-6l1 1-2 5zM24 16c0-4-2-6-5-6l-1 1 2 5z" fill="#c9d1e3"/></svg>ABOUT</div>
      <div class="utility-link"><svg width="18" height="19" viewBox="0 0 18 19"><rect x="1" y="3" width="16" height="15" fill="none" stroke="#c9d1e3" stroke-width="2"/><rect x="1" y="3" width="16" height="4" fill="#c9d1e3"/><line x1="5" y1="0" x2="5" y2="4" stroke="#c9d1e3" stroke-width="2"/><line x1="13" y1="0" x2="13" y2="4" stroke="#c9d1e3" stroke-width="2"/></svg>EVENTS</div>
      <div class="utility-link"><svg width="18" height="18" viewBox="0 0 18 18"><circle cx="9" cy="9" r="6" fill="none" stroke="#c9d1e3" stroke-width="5" stroke-dasharray="3 1.7"/><circle cx="9" cy="9" r="4.5" fill="#c9d1e3"/><circle cx="9" cy="9" r="2" fill="#2a3a60"/></svg>ACCOUNT</div>
      <div class="utility-link"><svg width="16" height="18" viewBox="0 0 16 18"><path d="M3 1l3 4-2 2c1 3 3 5 5 6l2-2 4 3-2 3C7 17 1 10 1 3z" fill="#c9d1e3"/></svg>CONTACT</div>
    </nav>
  </header>

  <nav class="menu-bar">
    <ul>
      <li>Red Wine</li><li>White Wine</li><li>Sparkling</li><li>Rosé</li>
      <li>Old &amp; Rare</li><li>Stickies</li><li>Imported</li><li>Wine Club</li>
    </ul>
    <div class="cart">
      <svg width="28" height="24" viewBox="0 0 28 24"><path d="M0 2h5l4 14h15l3-10H7" fill="none" stroke="#fff" stroke-width="3" stroke-linejoin="round"/><rect x="8" y="6" width="17" height="8" fill="#fff"/><circle cx="11" cy="21" r="2.5" fill="#fff"/><circle cx="22" cy="21" r="2.5" fill="#fff"/></svg>
      Shopping cart is empty
    </div>
  </nav>

  <section class="tile courses">
    <div class="tile-photo" role="img" aria-label="Dimly lit wine course room with a long table and wine-lined shelves"></div>
    <div class="tile-kicker">EDUCATION</div>
    <div class="tile-title">WINE COURSES</div>
  </section>

  <section class="tile club">
    <div class="tile-photo" role="img" aria-label="Shop owner standing beside tall shelves of wine bottles"></div>
    <div class="tile-kicker">WINE CLUB</div>
    <div class="tile-title">Let Us CHOOSE</div>
    <div class="read-more">READ MORE</div>
  </section>

  <section class="tile packs">
    <div class="tile-photo" role="img" aria-label="Muted photograph of the cellar shopfront"></div>
    <div class="tile-kicker">PURCHASE</div>
    <div class="tile-title">MIXED PACKS</div>
  </section>

  <section class="promo shipping">
    <div class="promo-frame">
      <div class="promo-title">FREE SHIPPING</div>
      <div class="promo-sub">on orders over $200</div>
    </div>
  </section>

  <section class="promo newsletter">
    <div class="promo-frame">
      <div class="promo-title">NEWSLETTER</div>
      <div class="promo-sub">join the newsletter for specials</div>
    </div>
  </section>
</body>
</html>
```